Exclusive Wine Label for Australia

We require a new and exclusive wine label for one of our key clients. We are a family winery based in Western Australia with a premium focus. The wine will mainly be sold online so the label will require visual appeal and and a premium focus to fit a price point between $25-$30.

The label will be a revamp of an existing label of ours called Tallow Crest (bottle image attached) . The only criteria required is to use the name. It can have a totally new look and theme to it. When investigating concepts, look at what the region, Margaret River is know for. It's all about the coastal environment, natural appeal and the relaxed lifestyle that people enjoy when visiting.

The label should be vibrant, colorful and not too serious.

I've also attached one of our labels Tre Sorelle. This is to give you the structure and layout of how we want the label (please ignore the graphic design and the use of our brand Vendelli) . It's a single wrap label with the dimensions of 88mm tall x 170mm wide.

Our preference is to not use too many expensive finishes such as foils, but embossing and high builds are fine. Vendelli logo is not required and our winery will only be displayed in text where it shows where the product is made.

Target Market(s)

30-50 yrs. No specific gender, but more towards a feminine look

Requirements
Must have
• - Follow the layout of the Tre Sorelle Label attached.
- Tallow Crest as the Brand name on label. No reference to Vendelli required
- Fit the price point of $25-30
Nice to have
• It can have a retro look or it can be minimal and modern. I won't put examples up as we are looking for new concepts. Beach themed is the best approach and open to using people on the label as well. Otherwise you can explore making the text as the feature.
Should not have
• Swirls and Waves are overdone. Looking for something more creative.

```html
<!DOCTYPE html>
<html lang="en">
<head>
<meta charset="utf-8">
<title>Tallow Crest – 2017 Sauvignon Blanc Label</title>
<link rel="stylesheet" href="https://fonts.googleapis.com/css2?family=Amatic+SC:wght@700&family=Arimo:wght@400&display=swap">
<style>
  :root {
    --canvas-bg: #eef0f0;
    --label-paper: #ffffff;
    --ink: #1a1a1a;
    --art-sky: #a9d4e8;
    --art-violet: #a85ad0;
    --art-pink: #e78fc8;
    --art-amber: #e8b04a;
    --label-shadow: rgba(0, 0, 0, 0.08);
  }
  * { box-sizing: border-box; margin: 0; padding: 0; }
  html, body {
    width: 1000px;
    height: 1200px;
    overflow: hidden;
    background: var(--canvas-bg);
  }
  .canvas {
    position: relative;
    width: 1000px;
    height: 1200px;
    display: flex;
    align-items: center;
    justify-content: center;
  }
  .wine-label {
    position: relative;
    width: 940px;
    height: 487px;
    background: var(--label-paper);
    box-shadow: 0 2px 10px var(--label-shadow);
  }
  .label-front {
    position: absolute;
    left: 50%;
    top: 0;
    width: 420px;
    height: 100%;
    transform: translateX(-50%);
    text-align: center;
  }
  .mascot-art {
    position: absolute;
    left: 50%;
    top: 52px;
    width: 300px;
    height: 228px;
    transform: translateX(-50%);
    border-radius: 46% 50% 40% 44%;
    background:
      radial-gradient(circle at 55% 18%, var(--art-violet) 0 20%, transparent 40%),
      radial-gradient(circle at 80% 72%, var(--art-pink) 0 12%, transparent 28%),
      radial-gradient(circle at 45% 45%, var(--art-amber) 0 10%, transparent 30%),
      linear-gradient(160deg, var(--art-sky) 0%, #d9c8e6 55%, #f1e4ee 100%);
  }
  .brand-name {
    position: absolute;
    left: 0;
    right: 0;
    top: 300px;
    font-family: "Amatic SC", "Arial Narrow", sans-serif;
    font-weight: 700;
    font-size: 60px;
    line-height: 58px;
    letter-spacing: 3px;
    text-transform: uppercase;
    color: var(--ink);
  }
  .vintage-varietal {
    position: absolute;
    left: 0;
    right: 0;
    top: 428px;
    font-family: "Arimo", Arial, sans-serif;
    font-size: 15px;
    line-height: 18px;
    letter-spacing: 0.5px;
    color: var(--ink);
  }
</style>
</head>
<body>
  <main class="canvas">
    <section class="wine-label">
      <div class="label-front">
        <div class="mascot-art" role="img" aria-label="Space for the label's colourful watercolour mascot illustration"></div>
        <h1 class="brand-name">TALLOW<br>CREST</h1>
        <p class="vintage-varietal">2017 SAUVIGNON BLANC</p>
      </div>
    </section>
  </main>
</body>
</html>
```